New modern business card design

To design a brand new business card that's clean & modern in terms of layout.
I have attached our company logo and also basic information regarding what is needed on the card that also needs to be editable.

Target Market(s)

motor trade

Contact Information for Business Card

logo, name, title, tel, mob, email, address, www, all information is in the word.doc file

Requirements
Must have
• white background
Nice to have
• Nice clean font

```html
<!DOCTYPE html>
<html lang="en">
<head>
<meta charset="utf-8">
<title>Torque Lift Ltd – Business Card</title>
<link href="https://fonts.googleapis.com/css2?family=Arimo:wght@400;700&display=swap" rel="stylesheet">
<style>
  :root {
    --brand-blue: #1a6fb0;
    --brand-grey: #a7a9ac;
    --ink-grey: #6d6e71;
    --paper: #ffffff;
    --canvas: #eceef0;
    --wash-blue: #b9d6e8;
    --wash-grey: #dfe1e3;
  }
  * { box-sizing: border-box; margin: 0; padding: 0; }
  html, body { width: 1200px; height: 801px; overflow: hidden; }
  body {
    background: var(--canvas);
    font-family: "Arimo", Arial, sans-serif;
    position: relative;
  }
  .card {
    position: absolute;
    top: 255px;
    width: 510px;
    height: 292px;
    background: var(--paper);
    overflow: hidden;
    box-shadow: 0 6px 18px rgba(0,0,0,0.15);
  }
  .card--front { left: 70px; }
  .card--back { left: 620px; }

  /* Front */
  .band-top { position: absolute; left: 0; top: 0; width: 100%; height: 28px; background: var(--brand-blue); }
  .band-bottom { position: absolute; left: 0; bottom: 0; width: 100%; height: 64px; background: var(--brand-blue); }
  .person { position: absolute; left: 34px; top: 44px; }
  .person__name { font-size: 42px; font-weight: 700; line-height: 1; letter-spacing: -0.5px; }
  .person__first { color: var(--brand-blue); }
  .person__last { color: var(--brand-grey); }
  .person__title { font-size: 13px; font-weight: 700; color: var(--brand-blue); margin-left: 128px; margin-top: 2px; }
  .contacts { position: absolute; left: 36px; top: 112px; list-style: none; }
  .contacts li { display: flex; align-items: center; height: 21px; font-size: 12.5px; color: var(--brand-blue); }
  .contacts svg { width: 12px; height: 12px; margin-right: 12px; fill: var(--ink-grey); flex: none; }
  .company-mark { position: absolute; right: 36px; top: 182px; display: flex; align-items: center; gap: 7px; }
  .company-mark__square { width: 14px; height: 14px; background: var(--brand-blue); }
  .company-mark__name { font-size: 14px; font-weight: 700; color: var(--brand-blue); }

  /* Back */
  .wash { position: absolute; inset: 0; background: linear-gradient(120deg, var(--wash-blue) 0%, var(--wash-grey) 55%, var(--paper) 100%); opacity: 0.7; }
  .brand { position: absolute; left: 30px; top: 100px; font-size: 40px; font-weight: 700; color: var(--brand-blue); letter-spacing: 1px; }
  .rule { position: absolute; left: 30px; height: 2px; background: var(--brand-blue); }
  .rule--upper { top: 160px; width: 420px; }
  .rule--lower { top: 240px; width: 450px; }
  .web { position: absolute; left: 50px; top: 198px; font-size: 22px; font-weight: 700; color: var(--brand-blue); }
</style>
</head>
<body>
  <section class="card card--front">
    <div class="band-top"></div>
    <div class="person">
      <p class="person__name"><span class="person__first">Daniel</span> <span class="person__last">Palmer</span></p>
      <p class="person__title">General Manager</p>
    </div>
    <ul class="contacts">
      <li><svg viewBox="0 0 24 24"><path d="M6.6 10.8a15 15 0 0 0 6.6 6.6l2.2-2.2a1 1 0 0 1 1-.25 11.4 11.4 0 0 0 3.6.57 1 1 0 0 1 1 1V20a1 1 0 0 1-1 1A17 17 0 0 1 3 4a1 1 0 0 1 1-1h3.5a1 1 0 0 1 1 1c0 1.25.2 2.45.57 3.57a1 1 0 0 1-.25 1z"/></svg>0161 555 0192</li>
      <li><svg viewBox="0 0 24 24"><path d="M7 1h10a2 2 0 0 1 2 2v18a2 2 0 0 1-2 2H7a2 2 0 0 1-2-2V3a2 2 0 0 1 2-2zm0 3v14h10V4z"/></svg>07700 900 418</li>
      <li><svg viewBox="0 0 24 24"><path d="M12 2a10 10 0 1 0 5 18.7l-1-1.7A8 8 0 1 1 20 12v1a2 2 0 0 1-4 0V7h-2v1a5 5 0 1 0 .9 7A4 4 0 0 0 22 13v-1A10 10 0 0 0 12 2zm0 13a3 3 0 1 1 0-6 3 3 0 0 1 0 6z"/></svg>dpalmer@torque-lift.co.uk</li>
      <li><svg viewBox="0 0 24 24"><path d="M12 3 2 12h3v9h5v-6h4v6h5v-9h3z"/></svg>Kestrel Road, Fairbridge, Manchester, M99 2QT</li>
      <li><svg viewBox="0 0 24 24"><path d="M12 2a10 10 0 1 0 0 20 10 10 0 0 0 0-20zm6.9 6h-3a15 15 0 0 0-1.4-3.9A8 8 0 0 1 18.9 8zM12 4a13 13 0 0 1 1.9 4h-3.8A13 13 0 0 1 12 4zM4.3 14a8 8 0 0 1 0-4h3.4a16 16 0 0 0 0 4zm.8 2h3a15 15 0 0 0 1.4 3.9A8 8 0 0 1 5.1 16zm3-8h-3a8 8 0 0 1 4.4-3.9A15 15 0 0 0 8.1 8zM12 20a13 13 0 0 1-1.9-4h3.8A13 13 0 0 1 12 20zm2.3-6H9.7a14 14 0 0 1 0-4h4.6a14 14 0 0 1 0 4zm.2 5.9a15 15 0 0 0 1.4-3.9h3a8 8 0 0 1-4.4 3.9zM16.3 14a16 16 0 0 0 0-4h3.4a8 8 0 0 1 0 4z"/></svg>www.torque-lift.co.uk</li>
    </ul>
    <div class="company-mark">
      <span class="company-mark__square"></span>
      <span class="company-mark__name">TORQUE LIFT LTD</span>
    </div>
    <div class="band-bottom"></div>
  </section>

  <section class="card card--back">
    <div class="wash" role="img" aria-label="Soft blue and grey background wash behind the company name"></div>
    <p class="brand">TORQUE LIFT LTD</p>
    <div class="rule rule--upper"></div>
    <p class="web">www.torque-lift.co.uk</p>
    <div class="rule rule--lower"></div>
  </section>
</body>
</html>
```